1" x 3" label needed for essential oil bottle(s) - new ecommerce company

We need a label designed for 10 ml bottles of essential oils. We are offering 9 different types of essential oil: Lavender, Cedarwood, Eucalyptus, Frankincense, Lemon, Orange, Peppermint, Rosemary, and Tea Tree. The label should have a space for the type of essential oil. The bottles are an amber color (am including a photo) as essential oils are sensitive to light. also am including an AI file of our logo, which we'd like included on the label; the logo file also contains our logo colors, a dark blue and light grey. We'd also like the following on the label: "CAUTION: EYE AND SKIN IRRITANT. Avoid contact with eyes and skin. Wash hands after handling. If eye contact occurs, flush with water for 15 minutes. Not intended for topical or internal use. Contains Essential Oils. KEEP OUT OF REACH OF CHILDREN."
Also "Ingredients: 100% pure essential oil, GC tested."
Also "0.33 fl oz (10 ml)
Finally, we will need to include a sideways bar code on the right side of the label, so need 3/8" of white space on the right of the label.
We'd like the label to be calming, but modern, friendly, and confident.

```html
<!DOCTYPE html>
<html lang="en">
<head>
<meta charset="utf-8">
<title>Calmere Lavender Essential Oil Label</title>
<link rel="stylesheet" href="https://fonts.googleapis.com/css2?family=Cormorant+Garamond:ital,wght@0,500;1,500&family=Crimson+Text:ital,wght@0,400;0,600;1,400&family=Montserrat:wght@500&display=swap">
<style>
  :root {
    --slate: #424f58;
    --ivory: #f1f0ed;
    --mist: #e4e4e2;
    --paper: #ffffff;
  }
  * { margin: 0; padding: 0; box-sizing: border-box; }
  html, body { width: 1200px; height: 845px; overflow: hidden; background: var(--paper); }
  .canvas { position: relative; width: 1200px; height: 845px; background: var(--paper); }
  .label {
    position: absolute; left: 0; top: 191px; width: 1200px; height: 515px;
    background: var(--slate); overflow: hidden; color: var(--ivory);
  }
  .foliage { position: absolute; }
  .foliage--top { left: 286px; top: 0; width: 205px; height: 152px;
    background: radial-gradient(ellipse at 50% 20%, rgba(241,240,237,0.16), rgba(79,98,108,0.25) 60%, rgba(66,79,88,0) 80%); }
  .foliage--bottom { left: 697px; top: 278px; width: 212px; height: 237px;
    background: radial-gradient(ellipse at 50% 70%, rgba(241,240,237,0.16), rgba(79,98,108,0.25) 60%, rgba(66,79,88,0) 80%); }
  .centered { position: absolute; text-align: center; transform: translateX(-50%); white-space: nowrap; }
  .brand-mark { position: absolute; left: 574px; top: 56px; width: 46px; height: 46px;
    border: 1.5px solid var(--ivory); border-radius: 50%; }
  .brand-name { left: 597px; top: 168px; font-family: "Cormorant Garamond", serif; font-weight: 500;
    font-size: 48px; letter-spacing: 0.3em; line-height: 1; padding-left: 0.3em; }
  .tagline { left: 598px; top: 226px; font-family: "Montserrat", sans-serif; font-weight: 500;
    font-size: 13px; letter-spacing: 0.48em; line-height: 28px; padding-left: 0.48em; }
  .oil-name { left: 591px; top: 321px; font-family: "Cormorant Garamond", serif; font-style: italic;
    font-weight: 500; font-size: 52px; line-height: 56px; }
  .oil-type { position: absolute; left: 517px; top: 379px; width: 136px; height: 28px;
    background: var(--mist); color: var(--slate); font-family: "Crimson Text", serif; font-weight: 600;
    font-size: 21px; line-height: 28px; text-align: center; }
  .volume { left: 582px; top: 458px; font-family: "Crimson Text", serif; font-size: 19px; line-height: 26px; letter-spacing: 0.03em; }
  .caution { left: 214px; top: 189px; font-family: "Crimson Text", serif; font-style: italic; font-size: 21px; line-height: 26px; }
  .caution-title { font-size: 20px; font-weight: 400; margin-bottom: 13px; letter-spacing: -0.01em; }
  .info { left: 1003px; top: 114px; font-family: "Crimson Text", serif; font-style: italic; font-size: 21px; line-height: 26px; }
  .info .ingredients { margin-bottom: 25px; }
  .info .ingredients span { display: block; }
  .info .usage { margin-bottom: 31px; }
  .info .contains { margin-bottom: 38px; }
  .info .warning { font-size: 19px; letter-spacing: -0.01em; }
  .barcode-space { position: absolute; left: 977px; top: 434px; width: 216px; height: 81px; background: var(--mist); }
</style>
</head>
<body>
<div class="canvas">
  <section class="label">
    <div class="foliage foliage--top" role="img" aria-label="Line-drawn leafy botanical sprig hanging from the top edge"></div>
    <div class="foliage foliage--bottom" role="img" aria-label="Line-drawn leafy botanical sprig rising from the bottom edge"></div>

    <div class="caution centered">
      <h2 class="caution-title">CAUTION: EYE AND SKIN IRRITANT</h2>
      <p>Avoid contact with eyes and skin.<br>Wash hands after handling.</p>
      <p>If eye contact occurs, flush with<br>water for 15 minutes.</p>
    </div>

    <div class="brand-mark"></div>
    <h1 class="brand-name centered">CALMERE</h1>
    <p class="tagline centered">ROOTED IN CALM<br>MADE SIMPLY</p>

    <p class="oil-name centered">Lavender</p>
    <p class="oil-type">Essential Oil</p>
    <p class="volume centered">0.33 fl oz (10 ml)</p>

    <div class="info centered">
      <p class="ingredients"><span>Ingredients:</span><span>100% pure essential oil, GC tested.</span></p>
      <p class="usage">Not intended for topical or internal use.</p>
      <p class="contains">Contains Essential Oils.</p>
      <p class="warning">KEEP OUT OF REACH OF CHILDREN.</p>
    </div>

    <div class="barcode-space"></div>
  </section>
</div>
</body>
</html>
```